Fresh Start Credit Guide - Banner Ad for CA Website

I need a banner ad for a book I'm selling.

The book is about Fresh Start Credit Guide, that is a County Court Judgment, from a credit report.

I have two websites. I want the banner ad to appear on
www.cardenashby.co.uk

It will then link to the new site: https://freshstartcreditguide.co.uk/

The first site already has a lot of traffic from visitors wanting to remove a CCJ. The purpose of that first site was originally for visitors to become clients of the law firm. However, most visitors can't afford legal advice and so I'd like to offer them the book instead.

I would like to see designs that use the colour green. The final design should communicate financial freedom, simplicity and trustworthiness.

Target Market(s)

Individuals who have discovered a CCJ on their credit report

Industry/Entity Type

Law

Font styles to use
Sans Serif

Colors
0054AA
0677BA
7BADD7
CADEEF
E8F1F8
0094D4
00A9DD
6FCCEA
C7EBF8
E9F6FB
00AB8E
00BBA5
67D7C9
C6EFE9
E9F9F6

Requirements
Must have
• Must fit at the end of a blog article, such as this one https://www.cardenashby.co.uk/ccj-wrong-address/

```html
<!DOCTYPE html>
<html lang="en">
<head>
<meta charset="utf-8">
<title>Fresh Start Credit Guide – Banner</title>
<link rel="stylesheet" href="https://fonts.googleapis.com/css2?family=Anton&family=Montserrat:wght@400;500;700;800&display=swap">
<style>
  :root {
    --green: #14a98c;
    --red: #e41f2d;
    --red-dark: #9e1019;
    --ink: #151219;
    --white: #ffffff;
    --strip: #f1f1ef;
    --grey: #4a4a4a;
    --teal-text: #0f9e83;
  }
  * { box-sizing: border-box; margin: 0; padding: 0; }
  html, body { width: 1200px; height: 1200px; overflow: hidden; background: var(--white); }
  body { position: relative; font-family: "Montserrat", sans-serif; }

  .banner {
    position: absolute; left: 82px; top: 387px; width: 1045px; height: 435px;
    background: var(--green);
    box-shadow: 0 10px 28px rgba(0,0,0,0.35);
    overflow: hidden;
  }
  .banner__strip {
    position: absolute; left: 0; top: 347px; width: 100%; height: 76px;
    background: var(--strip);
  }

  .title { position: absolute; left: 51px; top: 28px; line-height: 1; font-weight: normal; }
  .title__top { font-weight: 800; font-size: 37px; color: var(--ink); letter-spacing: 1px; }
  .title__mid { margin-top: 10px; font-weight: 800; font-size: 58px; color: var(--red); letter-spacing: -0.5px; }
  .title__big { margin-top: 18px; font-family: "Anton", sans-serif; font-size: 118px; color: var(--ink); letter-spacing: 1px; line-height: 0.95; }

  .hero-photo {
    position: absolute; left: 322px; top: 122px; width: 198px; height: 188px;
    border-radius: 6px;
    background: linear-gradient(180deg, #5fae3c 0%, #6fae4a 35%, #a27a3c 60%, #8c6428 100%);
    opacity: 0.85;
  }

  .pitch {
    position: absolute; left: 543px; top: 22px; width: 192px;
    font-size: 15px; line-height: 18.5px; color: var(--white); font-weight: 500;
  }
  .pitch__rule { position: absolute; left: 543px; top: 185px; width: 45px; height: 3px; background: var(--white); }
  .author { position: absolute; left: 543px; top: 209px; line-height: 1; }
  .author__label { font-weight: 700; font-size: 22px; color: var(--red); letter-spacing: 0.5px; }
  .author__name { margin-top: 12px; font-weight: 800; font-size: 29px; color: var(--white); line-height: 1.05; letter-spacing: 0.3px; }

  .book-mockup {
    position: absolute; left: 755px; top: 54px; width: 254px; height: 268px;
    border-radius: 4px;
    background: linear-gradient(135deg, #f4f4f4 0%, #e8e8e8 55%, #cfd4d3 100%);
    box-shadow: 4px 8px 18px rgba(0,0,0,0.25);
  }

  .cta {
    position: absolute; left: 51px; top: 335px; width: 213px; height: 37px;
    background: var(--red); border-radius: 6px; text-decoration: none;
    color: var(--white); font-weight: 700; font-size: 25px; line-height: 37px; text-align: center;
  }
  .cta__fold {
    position: absolute; left: 35px; top: 335px; width: 24px; height: 16px;
    background: var(--red-dark); border-radius: 8px 0 0 8px;
  }
  .site-url {
    position: absolute; left: 48px; top: 381px;
    font-weight: 700; font-size: 22px; color: var(--teal-text); letter-spacing: 1.2px;
  }

  .availability { position: absolute; left: 549px; top: 363px; line-height: 1; }
  .availability__head { font-weight: 800; font-size: 22px; color: var(--red); }
  .availability__sub { margin-top: 8px; font-size: 13px; color: var(--grey); font-weight: 500; }

  .retailer {
    position: absolute; left: 830px; top: 363px;
    font-weight: 800; font-size: 36px; color: var(--ink); line-height: 1;
  }
</style>
</head>
<body>
  <section class="banner" aria-label="Fresh Start Credit Guide book banner">
    <div class="banner__strip"></div>

    <h1 class="title">
      <div class="title__top">FRESH START</div>
      <div class="title__mid">CREDIT</div>
      <div class="title__big">GUIDE</div>
    </h1>

    <div class="hero-photo" role="img" aria-label="Photo of young green plants growing from two stacks of coins"></div>

    <p class="pitch">A simple jargon-free guide to removing a County Court Judgment from your credit record, improving your credit score and finding financial freedom.</p>
    <div class="pitch__rule"></div>
    <div class="author">
      <div class="author__label">BOOK BY</div>
      <div class="author__name">DANIEL<br>HARTWELL</div>
    </div>

    <div class="book-mockup" role="img" aria-label="Book cover shown as paperback, tablet and phone editions"></div>

    <div class="cta__fold"></div>
    <a class="cta" href="https://freshstartcreditguide.co.uk/">BOOK NOW</a>
    <div class="site-url">www.freshstartcreditguide.co.uk</div>

    <div class="availability">
      <div class="availability__head">AVAILABLE NOW</div>
      <div class="availability__sub">In paperback and as an e-book.</div>
    </div>
    <div class="retailer">Bookvale</div>
  </section>
</body>
</html>
```